Flyer-Design TorvelMax Endkunde
Zielgruppe
Die Online-Plattform TorvelMax vermittelt dem Endkunden einen ServicePartner bei welchem er seine beschädigten Felgen professionell nach vorgegebenen gesetzlichen Richtlinien reparieren bzw. aufbereiten lassen kann. Ganz ohne großen Aufwand für den Kunden und zu erschwinglichen Preisen. Zielgruppe sind also Fahrzeugbesitzer mit beschädigten Alufelgen.
Aufgabenstellung
Design soll einen Wiedererkennungswert zur Website www.torvelmax.com (Bitte direkt in die Browser Suche eingeben, Website ist erst seit heute online) darstellen. Der Flyer wird von den ServicePartnern zur Kundenansprache verwendet.
Texte siehe pdf.
Auf der Website verwendetes Bildmaterial kann zur Verfügung gestellt werden. Sonst gerne Alternativ-Vorschläge für Stock-Fotos.
TorvelMax Logo und Styleguide siehe Anhang.

```html
<!DOCTYPE html>
<html lang="de">
<head>
<meta charset="utf-8">
<title>TorvelMax Flyer Endkunde</title>
<link rel="stylesheet" href="https://fonts.googleapis.com/css2?family=Archivo+Black&family=Arimo:wght@400;700&family=Questrial&display=swap">
<style>
  :root {
    --stage: #5b5b5d;
    --panel-dark: #48484a;
    --band-light: #d9d9db;
    --band-mid: #8e8e90;
    --frame: #cfcfd1;
    --red: #c8161e;
    --red-deep: #8e0d12;
    --white: #ffffff;
    --photo-night: #1c2636;
    --photo-blue: #3b5878;
  }
  * { margin: 0; padding: 0; box-sizing: border-box; }
  html, body { width: 867px; height: 1200px; overflow: hidden; }
  body { background: var(--stage); position: relative; font-family: "Arimo", Arial, sans-serif; color: var(--white); }

  .flyer { position: absolute; left: 0; top: 166px; width: 867px; height: 867px; background: var(--panel-dark); overflow: hidden; }
  .flyer-art { position: absolute; inset: 0; }

  .brand { position: absolute; left: 30px; top: 70px; display: flex; align-items: center; gap: 8px; }
  .brand-dot { width: 22px; height: 22px; border-radius: 50%; background: var(--red); }
  .brand-name { font-family: "Arimo", Arial, sans-serif; font-weight: 700; font-size: 24px; color: var(--red); }

  .headline { position: absolute; left: 29px; top: 366px; font-family: "Archivo Black", "Arial Black", sans-serif; font-size: 44px; line-height: 55px; letter-spacing: -0.5px; color: var(--white); text-shadow: 2px 2px 0 #5f5f61, 3px 3px 4px rgba(0,0,0,.45); text-transform: uppercase; }

  .feature { position: absolute; width: 250px; }
  .feature-title { font-weight: 700; font-size: 13.5px; line-height: 16px; }
  .feature-text { font-size: 12.5px; line-height: 15px; margin-top: 16px; }
  .feature-icon { position: absolute; width: 60px; height: 60px; }
  .f1 { left: 29px; top: 554px; }
  .f2 { left: 299px; top: 554px; }
  .f3 { left: 31px; top: 688px; }
  .f4 { left: 299px; top: 688px; }
  .f3 .feature-text { margin-top: 22px; }
  .f4 .feature-text { margin-top: 22px; }

  .contact { position: absolute; left: 578px; top: 634px; font-family: "Questrial", "Century Gothic", sans-serif; }
  .contact-heading { font-family: "Arimo", Arial, sans-serif; font-size: 21px; line-height: 26px; }
  .contact-line { display: flex; align-items: center; gap: 8px; font-size: 17.5px; line-height: 24px; }
  .contact-line svg { width: 16px; height: 16px; flex: none; }
  .contact-company { font-size: 19px; line-height: 24px; margin: 8px 0 4px 26px; }
  .contact-address { display: flex; gap: 8px; font-size: 17.5px; line-height: 22px; }
  .contact-address svg { width: 16px; height: 18px; flex: none; margin-top: 2px; }
  .first-line { margin-top: 6px; }
</style>
</head>
<body>
<section class="flyer">
  <svg class="flyer-art" width="867" height="867" viewBox="0 0 867 867">
    <defs>
      <radialGradient id="photoCar" cx="0.55" cy="0.55" r="0.7">
        <stop offset="0" stop-color="#2a3342"/>
        <stop offset="0.55" stop-color="var(--photo-night)"/>
        <stop offset="1" stop-color="var(--photo-blue)"/>
      </radialGradient>
      <linearGradient id="photoHex" x1="0" y1="0" x2="1" y2="1">
        <stop offset="0" stop-color="#6c7480"/>
        <stop offset="1" stop-color="#2c3038"/>
      </linearGradient>
      <linearGradient id="photoSeat" x1="0" y1="0" x2="1" y2="1">
        <stop offset="0" stop-color="#3a3d44"/>
        <stop offset="0.5" stop-color="#b58d52"/>
        <stop offset="1" stop-color="#2a2c31"/>
      </linearGradient>
      <radialGradient id="redBadge" cx="0.4" cy="0.35" r="0.7">
        <stop offset="0" stop-color="var(--red)"/>
        <stop offset="1" stop-color="var(--red-deep)"/>
      </radialGradient>
    </defs>

    <g role="img" aria-label="Foto: schwarzer Sportwagen mit Alufelge vor beleuchteten Bürogebäuden bei Nacht">
      <polygon points="0,0 867,0 867,200 434,478 0,205" fill="url(#photoCar)"/>
    </g>
    <polygon class="logo-panel" points="0,0 197,0 197,279 0,157" fill="rgba(255,255,255,.78)"/>
    <polygon class="band-light" points="0,205 434,478 867,200 867,228 434,506 0,233" fill="var(--band-light)"/>
    <polygon class="band-mid" points="0,233 434,506 867,228 867,258 434,532 0,262" fill="var(--band-mid)"/>

    <polygon class="hex-frame" points="614,108 670,29 782,29 838,108 782,187 670,187" fill="var(--frame)"/>
    <g role="img" aria-label="Foto: Hand im weißen Handschuh prüft eine schwarze Felge">
      <polygon points="630,108 678,42 774,42 822,108 774,174 678,174" fill="url(#photoHex)"/>
    </g>
    <polygon class="hex-frame" points="556,298 612,219 724,219 780,298 724,377 612,377" fill="var(--frame)"/>
    <g role="img" aria-label="Foto: zwei Mechaniker montieren ein Rad in der Werkstatt">
      <polygon points="572,298 620,232 716,232 764,298 716,364 620,364" fill="url(#photoHex)"/>
    </g>
    <polygon class="hex-frame" points="605,493 661,414 773,414 829,493 773,572 661,572" fill="var(--frame)"/>
    <g role="img" aria-label="Foto: Teddybär angeschnallt auf einem Autositz">
      <polygon points="621,493 669,427 765,427 813,493 765,559 669,559" fill="url(#photoSeat)"/>
    </g>

    <g class="feature-icon-set" fill="none" stroke="var(--white)" stroke-width="2">
      <circle cx="214" cy="572" r="30" fill="url(#redBadge)" stroke="none"/>
      <path d="M198 578 h30 v-7 l-5 -7 h-20 l-5 7 z M203 578 v4 M223 578 v4"/>
      <circle cx="512" cy="572" r="30" fill="url(#redBadge)" stroke="none"/>
      <circle cx="512" cy="574" r="13"/>
      <circle cx="512" cy="574" r="3"/>
      <path d="M512 561 v10 M512 577 v10 M499 574 h10 M515 574 h10"/>
      <circle cx="213" cy="711" r="30" fill="url(#redBadge)" stroke="none"/>
      <circle cx="207" cy="707" r="11"/>
      <path d="M207 696 v22 M196 707 h22"/>
      <circle cx="221" cy="717" r="5"/>
      <path d="M225 721 l6 6"/>
      <circle cx="512" cy="711" r="30" fill="url(#redBadge)" stroke="none"/>
      <rect x="502" y="697" width="20" height="27" fill="var(--white)" stroke="none"/>
      <circle cx="512" cy="711" r="5" stroke="var(--red)"/>
    </g>
  </svg>

  <div class="brand"><span class="brand-dot"></span><span class="brand-name">TorvelMax</span></div>

  <h1 class="headline">Kompetente<br>Fachgerechte<br>Felgenaufbereitung</h1>

  <div class="feature f1">
    <p class="feature-title">Felge beschädigt?<br>Wie ärgerlich!</p>
    <p class="feature-text">TorvelMax bietet Ihnen eine<br>schnelle und fachgerechte<br>Lösung – deutschlandweit!</p>
  </div>
  <div class="feature f2">
    <p class="feature-title">TorvelMax<br>ServicePartner finden</p>
    <p class="feature-text">Geben Sie Ihre Postleitzahl in die<br>Suche ein und wählen Sie den<br>für Sie optimalen TorvelMax<br>ServicePartner in Ihrer Nähe</p>
  </div>
  <div class="feature f3">
    <p class="feature-title">Felgenaufbereitung<br>buchen</p>
    <p class="feature-text">Buchen Sie Ihre<br>Felgenaufbereitung ganz einfach<br>bei Ihrem TorvelMax<br>ServicePartner, mit dem Sie<br>einen Aufbereitungsvertrag<br>schließen</p>
  </div>
  <div class="feature f4">
    <p class="feature-title">7 Werktage und<br>Felge(n) wie neu zurück</p>
    <p class="feature-text">Nach 7 Werktagen sind Ihre<br>Felge(n) wieder wie neu und<br>zurück bei Ihrem ServicePartner.<br>Nur noch abholen und bequem<br>vor Ort zahlen.</p>
  </div>

  <address class="contact" style="font-style:normal">
    <p class="contact-heading">Kontaktieren :</p>
    <p class="contact-line first-line">
      <svg viewBox="0 0 16 16"><path d="M3 1 l3 0 l1 4 l-2 1.5 a9 9 0 0 0 4.5 4.5 l1.5 -2 l4 1 l0 3 a2 2 0 0 1 -2 2 A13 13 0 0 1 1 3 a2 2 0 0 1 2 -2z" fill="var(--red)"/></svg>
      +49 (0)30 555 812 46
    </p>
    <p class="contact-line">
      <svg viewBox="0 0 16 16"><rect x="1" y="3" width="14" height="10" fill="var(--red)"/><path d="M1 3 l7 6 l7 -6" stroke="var(--panel-dark)" fill="none" stroke-width="1.3"/></svg>
      support@torvelmax.com
    </p>
    <p class="contact-line">
      <svg viewBox="0 0 16 16" fill="none" stroke="var(--red)" stroke-width="1.3"><circle cx="8" cy="8" r="6.5"/><ellipse cx="8" cy="8" rx="3" ry="6.5"/><path d="M1.5 8 h13 M2.5 4.5 h11 M2.5 11.5 h11"/></svg>
      www.torvelmax.com
    </p>
    <p class="contact-company">BrisoLark GmbH</p>
    <div class="contact-address">
      <svg viewBox="0 0 16 18"><path d="M8 1 a6 6 0 0 1 6 6 c0 4 -6 10 -6 10 s-6 -6 -6 -10 a6 6 0 0 1 6 -6z" fill="var(--red)"/><circle cx="8" cy="7" r="2.3" fill="var(--panel-dark)"/></svg>
      <p>Lindenweg 12 14823<br>Neuhaldau bei Potsdam</p>
    </div>
  </address>
</section>
</body>
</html>
```